Audio and Video download site

I am looking for a good and beautiful website where users can be a able to download and upload musicial files and video file. Basically, there will be two categories. The first category for the music files( mp3, mva and other popular music files) while the second category will be for video files (mp4, wmv, divx and other files) users would be able to like and dislike a song/video. Users do not necessarily have to sign up for them to make you or download and upload files from the website. The website should be youthful.

```html
<!DOCTYPE html>
<html lang="en">
<head>
<meta charset="utf-8">
<title>TuneDeck – Watch, listen, share</title>
<link href="https://fonts.googleapis.com/css2?family=Quicksand:wght@300;400;500&display=swap" rel="stylesheet">
<style>
  :root{
    --wine:#7a0a17;
    --wine-dark:#5e0611;
    --ink:#1b1b1b;
    --paper:#f1f1f1;
    --white:#ffffff;
    --black:#000000;
    --night:#0c0c0c;
    --panel-line:#2a2a33;
  }
  *{box-sizing:border-box;margin:0;padding:0}
  html,body{width:688px;height:1200px;overflow:hidden}
  body{position:relative;background:var(--paper);font-family:'Quicksand',sans-serif;color:var(--ink);font-weight:300}
  a{color:inherit}

  /* Hero */
  .hero{position:absolute;left:0;top:0;width:688px;height:554px;overflow:hidden}
  .hero-photo{position:absolute;inset:0;background:linear-gradient(100deg,#c9c4c4 0%,#e0dcdc 25%,#b9b7bd 55%,#8e8a93 75%,#c7c0c2 100%)}
  .hero-shade{position:absolute;left:0;right:0;top:521px;height:33px;background:rgba(40,30,35,.55)}
  .account-bar{position:absolute;right:4px;top:13px;font-size:12px;display:flex;gap:22px}
  .account-bar em{text-decoration:underline}
  .brand{position:absolute;left:503px;top:40px;font-size:36px;font-weight:300;color:var(--ink);display:flex;align-items:center;gap:10px}
  .brand-mark{width:16px;height:16px;background:var(--wine)}
  .divider{position:absolute;left:444px;top:32px;width:3px;height:489px;background:var(--panel-line)}

  .player{position:absolute;left:12px;top:44px;width:421px;height:421px;border:1px solid var(--panel-line);border-radius:4px}
  .screen{position:absolute;left:5px;top:5px;width:409px;height:392px;background:var(--black)}
  .screen-stage{position:absolute;left:0;top:58px;width:409px;height:274px;background:radial-gradient(ellipse at 45% 25%,#d8d8d8 0%,#f4f4f4 45%,#fbfbfb 100%)}
  .welcome{position:absolute;left:61px;top:86px;font-size:24px;color:#555;letter-spacing:1px}
  .welcome-name{position:absolute;left:0;width:409px;text-align:center;top:112px;font-size:48px;color:var(--wine);padding-left:40px}
  .time{position:absolute;left:5px;top:404px;font-size:10px;font-weight:400}
  .progress{position:absolute;left:38px;top:409px;width:378px;height:7px;border-radius:4px;background:var(--wine)}
  .progress-done{position:absolute;left:0;top:0;width:42px;height:7px;border-radius:4px;background:var(--wine-dark);box-shadow:inset 0 0 0 2px #9c1a28}
  .controls{position:absolute;left:0;top:468px;width:440px;height:50px}
  .controls svg{position:absolute}

  .playlist{position:absolute;left:463px;top:91px;width:212px;height:415px;border:1px solid var(--panel-line);border-radius:4px;text-align:center;font-size:16px;font-weight:400}
  .playlist p{line-height:20px}
  .playlist .oops{margin-top:112px}
  .playlist .links{margin-top:20px;line-height:20px}

  /* Trending */
  .trending{position:absolute;left:0;top:554px;width:688px;height:276px;background:var(--paper)}
  .trending h2{position:absolute;left:0;width:664px;text-align:center;top:17px;font-size:19px;font-weight:300;word-spacing:4px}
  .clip{position:absolute;top:62px}
  .clip-thumb{height:167px}
  .clip-title{text-align:center;font-size:12px;font-weight:400;margin-top:7px;white-space:nowrap;overflow:hidden}
  .slide-btn{position:absolute;top:98px;width:33px;height:120px;background:rgba(255,255,255,.45)}

  /* Music */
  .music{position:absolute;left:0;top:830px;width:688px;height:225px;background:var(--night)}
  .music h3{position:absolute;left:27px;top:80px;font-size:40px;line-height:35px;font-weight:300;color:var(--wine);letter-spacing:2px;word-spacing:8px}
  .music p{position:absolute;left:27px;top:168px;font-size:24px;color:var(--white);letter-spacing:5px;font-weight:400}
  .headphones{position:absolute;left:486px;top:43px;width:172px;height:140px;border-radius:80px 80px 20px 20px;background:linear-gradient(180deg,#3a060c,#7a0a17)}

  /* Join */
  .join{position:absolute;left:10px;top:1055px;width:668px;height:114px;border:1px solid var(--ink);border-top:none;border-radius:0 0 4px 4px;text-align:right;padding-right:12px}
  .join h4{font-size:19px;font-weight:400;color:var(--wine);margin-top:12px;line-height:20px}
  .join .sub{font-size:11px;letter-spacing:.5px}
  .join .cta{position:absolute;right:12px;top:50px;width:106px;height:32px;background:var(--wine);border-radius:2px;color:#9a1d2a;font-size:12px;line-height:32px;text-align:center}
  .join .signin{position:absolute;right:14px;top:90px;font-size:10px;font-weight:400}

  .legal{position:absolute;left:0;width:688px;top:1177px;text-align:center;font-size:6.5px;line-height:8px;font-weight:500}
</style>
</head>
<body>

<section class="hero">
  <div class="hero-photo" role="img" aria-label="Street photo of a young man listening to earphones"></div>
  <div class="hero-shade"></div>

  <nav class="account-bar"><span>Signed in as <em>GUEST</em></span><span>Log In</span><span>Register</span></nav>
  <div class="brand">TuneDeck <span class="brand-mark"></span></div>
  <div class="divider"></div>

  <div class="player">
    <div class="screen">
      <div class="screen-stage">
        <div class="welcome">Welcome to</div>
        <div class="welcome-name">TuneDeck</div>
      </div>
    </div>
    <div class="time">00:04</div>
    <div class="progress"><div class="progress-done"></div></div>
  </div>

  <div class="controls">
    <svg style="left:26px;top:12px" width="14" height="24" viewBox="0 0 14 24"><path d="M0 8h5l9-8v24l-9-8H0z" fill="var(--wine)"/></svg>
    <svg style="left:145px;top:14px" width="30" height="22" viewBox="0 0 30 22"><path d="M15 0v22L0 11zM30 0v22L15 11z" fill="var(--wine)"/></svg>
    <svg style="left:199px;top:3px" width="45" height="45" viewBox="0 0 45 45"><circle cx="22.5" cy="22.5" r="22.5" fill="var(--wine)"/><path d="M16 11l18 11.5L16 34z" fill="var(--white)"/></svg>
    <svg style="left:268px;top:14px" width="30" height="22" viewBox="0 0 30 22"><path d="M0 0v22l15-11zM15 0v22l15-11z" fill="var(--wine)"/></svg>
    <svg style="left:317px;top:13px" width="25" height="25" viewBox="0 0 25 25"><circle cx="12.5" cy="12.5" r="8" fill="none" stroke="var(--wine)" stroke-width="5"/><circle cx="12.5" cy="12.5" r="10.5" fill="none" stroke="var(--wine)" stroke-width="4" stroke-dasharray="4 4.2"/></svg>
    <svg style="left:355px;top:15px" width="26" height="20" viewBox="0 0 26 20"><path d="M0 4h5c6 0 9 12 15 12h4M0 16h5c6 0 9-12 15-12h4" fill="none" stroke="var(--wine)" stroke-width="1.6"/><path d="M21 1l4 3-4 3M21 13l4 3-4 3" fill="none" stroke="var(--wine)" stroke-width="1.6"/></svg>
    <svg style="left:395px;top:12px" width="22" height="26" viewBox="0 0 22 26"><path d="M7 0h8v13h7L11 26 0 13h7z" fill="var(--wine)"/></svg>
  </div>

  <aside class="playlist">
    <p class="oops">Oh no!<br>Your playlist is empty.</p>
    <p class="links"><a href="#">Upload your videos now</a><br>or<br><a href="#">browse through our library</a></p>
  </aside>
</section>

<section class="trending">
  <h2>See what others are watching right now</h2>
  <div class="clip" style="left:0;width:241px">
    <div class="clip-thumb" style="background:linear-gradient(90deg,#000 0 12%,#b8a48e 12% 88%,#000 88%)" role="img" aria-label="Video still of a smiling pug sitting on a bed"></div>
    <div class="clip-title">Pug Smiling</div>
  </div>
  <div class="clip" style="left:251px;width:241px">
    <div class="clip-thumb" style="background:linear-gradient(180deg,#d9dcd4 0%,#c2c3ba 35%,#8d6a55 36%,#5a473c 100%)" role="img" aria-label="Video still of a hand about to strike a brick"></div>
    <div class="clip-title">How to break a brick with your hand</div>
  </div>
  <div class="clip" style="left:503px;width:185px">
    <div class="clip-thumb" style="background:linear-gradient(120deg,#d7775a 0%,#d9a3c4 50%,#3a2a2c 100%)" role="img" aria-label="Video still of a man blowing a huge bubblegum bubble"></div>
    <div class="clip-title" style="text-align:left;padding-left:35px">World Record Bubble Blo</div>
  </div>
  <div class="slide-btn" style="left:0"></div>
  <div class="slide-btn" style="right:0"></div>
</section>

<section class="music">
  <h3>Want to rock out<br>to a song instead?</h3>
  <p>Check out our music section!</p>
  <div class="headphones" role="img" aria-label="Red headphones illustration"></div>
</section>

<section class="join">
  <h4>Tired of creating a new playlist every time you visit?</h4>
  <div class="sub">Join in and save your playlist, upload videos, or experience the world's greatest moments on screen</div>
  <div class="cta">Create account</div>
  <div class="signin">Already have an account? <a href="#">Sign in</a>.</div>
</section>

<footer class="legal">Copyright © 2016 TuneDeck. Use of this website constitutes acceptance of our<br><a href="#">User Agreement</a> and <a href="#">Privacy Policy</a>.</footer>

</body>
</html>
```